Australian Web Design company needs a business card design

We need a business card design for a Sydney based Web Design/Development company called "Blue Pine Web Design". We design, build and deploy websites for small to medium sized businesses. The final design should be clean and communicate that we are a professional and supportive company.
I'd like the Icon to be abstract. Something that embodies the power of the internet, needs to be clean/professional and show that we are human and that we support our customers. Hope that helps.
Target Market(s)
All small to medium businesses
Industry/Entity Type
Business
Contact Information for Business Card
Gordon Whitcombe
Blue Pine Web Design
17 Calloway Brook Road
East Gosford
NSW 2250
0438 572 614
gordon@bluepinewebdesign.com.au
www.bluepinewebdesign.com.au

```html
<!DOCTYPE html>
<html lang="en">
<head>
<meta charset="utf-8">
<title>Blue Pine Web Design – Business Card</title>
<link rel="stylesheet" href="https://fonts.googleapis.com/css2?family=Arimo:wght@400;500&display=swap">
<style>
  :root {
    --page: #ffffff;
    --card-blue: #1e7af5;
    --ribbon: #45f2a6;
    --ribbon-fold: #37d08e;
    --green: #86f41c;
    --yellow: #ffcb22;
    --red: #ff2d0a;
    --pink: #ff2fb4;
    --purple: #9933ff;
    --white: #ffffff;
    --label: #111111;
  }
  * { margin: 0; padding: 0; box-sizing: border-box; }
  html, body { width: 1200px; height: 900px; overflow: hidden; background: var(--page); }
  body { position: relative; font-family: "Arimo", Arial, sans-serif; }

  .card { position: absolute; width: 674px; height: 385px; background: var(--card-blue); overflow: hidden; }
  .card--front { left: 258px; top: 28px; }
  .card--back { left: 255px; top: 470px; width: 673px; }
  .card__art { position: absolute; inset: 0; width: 100%; height: 100%; }

  .holder-name {
    position: absolute; left: 112px; top: 56px;
    font-size: 41px; font-weight: 400; color: var(--white); letter-spacing: -0.5px;
  }
  .contact-list { position: absolute; left: 121px; top: 0; list-style: none; color: var(--white); font-size: 23px; letter-spacing: -0.2px; }
  .contact-list li { position: absolute; left: 0; white-space: nowrap; line-height: 1; transform: translateY(-50%); }

  .search-bar {
    position: absolute; left: 144px; top: 178px; width: 438px; height: 47px;
    border: 2px solid var(--white); border-radius: 24px;
    color: var(--white); font-size: 26px; letter-spacing: -0.3px; text-align: center; line-height: 43px;
  }

  .side-label { position: absolute; font-size: 22px; color: var(--label); letter-spacing: 0.5px; transform: translateX(-50%); }
  .side-label--front { left: 562px; top: 423px; }
  .side-label--back { left: 609px; top: 864px; }
</style>
</head>
<body>

<section class="card card--front" aria-label="Business card front">
  <svg class="card__art" viewBox="0 0 674 385" aria-hidden="true">
    <polygon points="674,175 430,385 674,385" fill="#ffffff" opacity="0.05"/>
    <line x1="505" y1="0" x2="674" y2="175" stroke="#ffffff" stroke-width="9" opacity="0.1"/>
    <line x1="674" y1="170" x2="420" y2="385" stroke="#ffffff" stroke-width="6" opacity="0.1"/>
    <line x1="600" y1="140" x2="674" y2="250" stroke="#ffffff" stroke-width="4" opacity="0.08"/>
    <rect x="0" y="0" width="60" height="29" fill="var(--green)"/>
    <rect x="60" y="0" width="67" height="29" fill="var(--yellow)"/>
    <rect x="127" y="0" width="69" height="29" fill="var(--red)"/>
    <rect x="196" y="0" width="69" height="29" fill="var(--pink)"/>
    <rect x="265" y="0" width="409" height="29" fill="var(--purple)"/>
    <rect x="0" y="89" width="57" height="28" fill="var(--ribbon)"/>
    <rect x="55" y="89" width="59" height="296" fill="var(--ribbon)"/>
    <polygon points="55,89 80,89 114,117 55,117" fill="var(--ribbon-fold)"/>
    <g class="icon icon--company">
      <circle cx="83" cy="152" r="20" fill="var(--green)" stroke="#2a9a3a" stroke-width="1.5"/>
      <rect x="73" y="141" width="11" height="21" fill="#fff"/>
      <rect x="84" y="148" width="9" height="14" fill="#fff"/>
      <g fill="var(--green)"><rect x="75" y="144" width="3" height="3"/><rect x="79" y="144" width="3" height="3"/><rect x="75" y="149" width="3" height="3"/><rect x="79" y="149" width="3" height="3"/><rect x="75" y="154" width="3" height="3"/><rect x="79" y="154" width="3" height="3"/><rect x="87" y="152" width="3" height="3"/></g>
    </g>
    <g class="icon icon--address">
      <circle cx="83" cy="199" r="20" fill="var(--yellow)" stroke="#b8860b" stroke-width="1.5"/>
      <path d="M83 213 L75 199 A9 9 0 1 1 91 199 Z" fill="#fff"/>
      <circle cx="83" cy="194" r="3.5" fill="var(--yellow)"/>
    </g>
    <g class="icon icon--phone">
      <circle cx="83" cy="247" r="20" fill="var(--red)" stroke="#a01800" stroke-width="1.5"/>
      <path d="M76 236 l5 -1 l3 7 l-3 2 q2 5 6 8 l2 -3 l7 3 l-1 5 q-6 2 -13 -5 q-7 -8 -6 -16 z" fill="#fff"/>
    </g>
    <g class="icon icon--email">
      <circle cx="83" cy="296" r="20" fill="var(--pink)" stroke="#a0126e" stroke-width="1.5"/>
      <rect x="72" y="288" width="22" height="15" fill="none" stroke="#fff" stroke-width="2"/>
      <polyline points="72,288 83,297 94,288" fill="none" stroke="#fff" stroke-width="2"/>
    </g>
    <g class="icon icon--web">
      <circle cx="83" cy="344" r="20" fill="var(--purple)" stroke="#5a1399" stroke-width="1.5"/>
      <g fill="none" stroke="#fff" stroke-width="1.6">
        <circle cx="83" cy="344" r="12"/>
        <ellipse cx="83" cy="344" rx="5" ry="12"/>
        <line x1="71" y1="344" x2="95" y2="344"/>
        <line x1="83" y1="332" x2="83" y2="356"/>
        <path d="M73 338 h20 M73 350 h20"/>
      </g>
    </g>
  </svg>
  <h1 class="holder-name">Gordon Whitcombe</h1>
  <ul class="contact-list">
    <li style="top:151px">Blue Pine Web Design</li>
    <li style="top:201px">17 Calloway Brook Road West Ferndale NSW 2291</li>
    <li style="top:247px">0438 572 614</li>
    <li style="top:296px">gordon@bluepinewebdesign.com.au</li>
    <li style="top:344px">www.bluepinewebdesign.com.au</li>
  </ul>
</section>
<p class="side-label side-label--front">FRONT</p>

<section class="card card--back" aria-label="Business card back">
  <svg class="card__art" viewBox="0 0 673 385" aria-hidden="true">
    <rect x="0" y="0" width="408" height="25" fill="var(--purple)"/>
    <rect x="408" y="0" width="70" height="25" fill="var(--pink)"/>
    <rect x="478" y="0" width="68" height="25" fill="var(--red)"/>
    <rect x="546" y="0" width="67" height="25" fill="var(--yellow)"/>
    <rect x="613" y="0" width="60" height="25" fill="var(--green)"/>
    <g class="icon icon--search" fill="none" stroke="#fff" stroke-width="2.5">
      <circle cx="106" cy="195" r="12"/>
      <line x1="115" y1="204" x2="128" y2="217" stroke-width="3.5" stroke-linecap="round"/>
    </g>
  </svg>
  <div class="search-bar">www.bluepinewebdesign.com.au</div>
</section>
<p class="side-label side-label--back">BACK</p>

</body>
</html>
```